Business Card & Letterhead Design

We a financial advice company based in Australia. We provide advice to wealthy farmers.

We are changing our business name FROM Palomar Financial TO Bluegate Wealth and we need a new letterhead and double sided business card design

Attached is designs from our previous branding (Palomar Financial) as it includes all the details we require on the new Bluegate Wealth business cards and letterhead.

```html
<!DOCTYPE html>
<html lang="en">
<head>
<meta charset="utf-8">
<title>Bluegate Wealth Stationery</title>
<link rel="stylesheet" href="https://fonts.googleapis.com/css2?family=Poppins:ital,wght@0,400;0,600;1,400&family=Roboto:wght@300;400&family=EB+Garamond:ital@0;1&display=swap">
<style>
:root{
  --backdrop:#dedede;
  --charcoal:#404040;
  --paper:#f1f1f2;
  --ink:#3a3a3a;
  --ink-soft:#5b5b5b;
  --on-dark:#f2f2f2;
  --on-dark-soft:#cfcfcf;
}
*{margin:0;padding:0;box-sizing:border-box}
html,body{width:1200px;height:1027px;overflow:hidden;background:var(--backdrop)}
body{position:relative;font-family:"Poppins",sans-serif;color:var(--ink)}
.icon{width:7px;height:7px;fill:currentColor;flex:none}

/* Letterhead */
.letterhead{position:absolute;left:484px;top:96px;width:583px;height:821px;display:flex;background:var(--paper);box-shadow:0 14px 28px rgba(0,0,0,.12)}
.letterhead-band{width:192px;background:var(--charcoal);color:var(--on-dark);padding:37px 16px 0 31px;font-size:7.6px;line-height:9.4px}
.brand{display:flex;flex-direction:column;align-items:center;margin-left:-15px;width:176px}
.brand-circle{width:37px;height:37px;border:1.5px solid currentColor;border-radius:50%}
.brand-name{font-size:12px;letter-spacing:.5px;margin-top:4px;font-weight:400;white-space:nowrap}
.brand-tag{font-size:5px;letter-spacing:1.6px;text-transform:uppercase;margin-top:1px;color:var(--on-dark-soft)}
.entity{margin-top:26px}
.contact-group{margin-top:13px}
.contact-row{display:flex;gap:4px;align-items:flex-start}
.contact-row .icon{margin-top:1px}
.contact-group + .contact-group{margin-top:6px}
.motto{margin-top:14px}
.motto-title{font-weight:600;font-size:9px;line-height:11px}
.motto-sub{font-style:italic;font-size:8.4px}
.licensee{margin-top:22px}

.letterhead-body{flex:1;padding:166px 62px 0 44px;font-family:"Roboto",sans-serif;font-weight:300;color:var(--ink-soft)}
.salutation{font-weight:400;font-size:14px;color:var(--ink);margin-bottom:21px}
.letterhead-body p{font-size:8.2px;line-height:12.2px;text-align:justify;margin-bottom:12.4px}
.sign-off{margin-top:20px;font-size:8.2px}
.signature{display:block;width:86px;height:46px;margin-top:6px;background:linear-gradient(90deg,rgba(40,40,40,.18),rgba(40,40,40,.06))}

/* Cards */
.card{position:absolute;left:140px;width:292px;height:167px;box-shadow:0 12px 22px rgba(0,0,0,.14)}
.card-front{top:543px;background:var(--paper);text-align:center;padding-top:33px}
.card-motto{font-weight:600;font-size:8px;line-height:9px}
.card-motto-sub{font-style:italic;font-size:6.6px;display:flex;align-items:center;justify-content:center;gap:4px}
.card-motto-sub::before,.card-motto-sub::after{content:"";width:14px;height:.6px;background:var(--ink)}
.card-person{display:flex;justify-content:center;margin-top:12px;gap:8px}
.person{text-align:right;padding-right:8px;border-right:.8px solid var(--ink);font-size:6px;line-height:7.4px;color:var(--ink-soft)}
.person-name{font-weight:600;font-size:9.6px;line-height:12px;color:var(--ink)}
.person-cred{color:var(--ink)}
.card-contacts{text-align:left;font-size:6px;line-height:8px;color:var(--ink-soft)}
.card-contacts .icon{width:5px;height:5px;margin-top:1.5px}
.card-address{margin-top:20px;font-size:6.2px;line-height:9px;color:var(--ink-soft)}
.card-address .contact-row{justify-content:center;gap:2px}
.card-address .icon{width:5px;height:5px;margin-top:2px}

.card-back{top:750px;background:var(--charcoal);color:var(--on-dark);text-align:center;padding-top:39px}
.card-back .brand{width:100%;margin-left:0}
.card-back .brand-circle{width:42px;height:42px}
.card-back .brand-name{font-size:14px}
.services{font-family:"EB Garamond",serif;font-size:7.6px;margin-top:13px}
.licensee-note{font-family:"EB Garamond",serif;font-style:italic;font-size:6px;line-height:8px;margin-top:4px;color:var(--on-dark-soft)}
.licensee-note span{display:block;width:180px;margin:0 auto;border-top:.5px solid var(--on-dark-soft);padding-top:1px}
</style>
</head>
<body>
<svg width="0" height="0" style="position:absolute" aria-hidden="true">
  <symbol id="i-pin" viewBox="0 0 10 10"><path d="M5 0a3.5 3.5 0 0 0-3.5 3.5C1.5 6 5 10 5 10s3.5-4 3.5-6.5A3.5 3.5 0 0 0 5 0zm0 5a1.4 1.4 0 1 1 0-2.8A1.4 1.4 0 0 1 5 5z"/></symbol>
  <symbol id="i-phone" viewBox="0 0 10 10"><path d="M2 .5l2 2-1.2 1.3a6 6 0 0 0 3.4 3.4L7.5 6l2 2-1.5 1.5C4 9.5.5 6 .5 2z"/></symbol>
  <symbol id="i-mobile" viewBox="0 0 10 10"><path d="M2.5 0h5v10h-5zM3.5 1v7h3V1z"/></symbol>
  <symbol id="i-fax" viewBox="0 0 10 10"><path d="M2.5 0h5v3h-5zM0 3.5h10v4H8V10H2V7.5H0zM3 6v3h4V6z"/></symbol>
  <symbol id="i-mail" viewBox="0 0 10 10"><path d="M0 2h10v.6L5 5.6 0 2.6zM0 3.8l5 3 5-3V8H0z"/></symbol>
  <symbol id="i-globe" viewBox="0 0 10 10"><path d="M5 0a5 5 0 1 0 0 10A5 5 0 0 0 5 0zm0 1.2c.8 0 1.5 1.6 1.6 3.2H3.4C3.5 2.8 4.2 1.2 5 1.2zM3.4 5.6h3.2C6.5 7.2 5.8 8.8 5 8.8S3.5 7.2 3.4 5.6z"/></symbol>
</svg>

<article class="letterhead">
  <aside class="letterhead-band">
    <div class="brand">
      <div class="brand-circle"></div>
      <div class="brand-name">BLUEGATE WEALTH</div>
      <div class="brand-tag">Strategic Financial Advice</div>
    </div>
    <div class="entity">Corvale Investments Pty Ltd<br>ATF The Westmere Investment<br>Trust T/AS Palomar Financial<br>ABN: 00 000 000 001<br>Corporate Authorised<br>Representative of Meridian<br>Advice Partners Limited</div>
    <div class="contact-group">
      <div class="contact-row"><svg class="icon"><use href="#i-pin"/></svg><span>Suite 4A, 18 Harlow St<br>Riverbend QLD 4100</span></div>
    </div>
    <div class="contact-group">
      <div class="contact-row"><svg class="icon"><use href="#i-pin"/></svg><span>PO Box 5521<br>Eastvale QLD 4100</span></div>
    </div>
    <div class="contact-group">
      <div class="contact-row"><svg class="icon"><use href="#i-phone"/></svg><span>(07) 3000 1234</span></div>
      <div class="contact-row"><svg class="icon"><use href="#i-fax"/></svg><span>(07) 3000 5678</span></div>
      <div class="contact-row"><svg class="icon"><use href="#i-mail"/></svg><span>admin@palomarfinancial.example</span></div>
      <div class="contact-row"><svg class="icon"><use href="#i-globe"/></svg><span>www.palomarfinancial.example</span></div>
    </div>
    <div class="motto">
      <div class="motto-title">FINANCIAL PEACE OF MIND</div>
      <div class="motto-sub">— A referral built business —</div>
    </div>
    <div class="licensee">Meridian Advice Partners Limited<br>ABN 00 000 000 002<br>Australian Financial Services Licence<br>Licence Number 000 111<br>Principle Address: 100 Example St<br>PO Box 1000 Melbourne VIC 3000</div>
  </aside>
  <section class="letterhead-body">
    <div class="salutation">Dear Mr. Carter,</div>
    <p>Lorem ipsum dolor sit amet, consectetur adipiscing elit. Donec orci purus, luctus vitae dignissim eu, iaculis sed purus. Vivamus faucibus, ipsum nec aliquet viverra, leo mauris condimentum ligula, sit amet sagittis enim ligula quis arcu. Nam egestas tortor id nisi porttitor mattis. In tortor ante, ultricies in suscipit a, tempus non massa. Vivamus et auctor mi. Fusce vel massa nulla. Phasellus nec eros mauris, et scelerisque orci.</p>
    <p>Donec malesuada orci vitae nulla accumsan porta a id massa. Quisque accumsan iaculis magna sit amet fringilla. Maecenas consequat, magna eget tincidunt semper, odio nibh rutrum mi, id feugiat ante nisi eu risus. Vestibulum nunc orci, rhoncus a placerat in, ultricies in mi. Cras mattis varius eros, vel fringilla nisi suscipit eget. Quisque scelerisque sagittis nulla at porttitor.</p>
    <p>Sed id augue vitae urna euismod commodo aliquet a quam. Pellentesque arcu velit, cursus et malesuada ut, consequat et diam. Nullam erat sem, rhoncus id ullamcorper vitae, rhoncus et arcu. In ultricies ultricies nulla, ut rutrum nisi iaculis at. Donec eu magna a metus ornare faucibus. Fusce aliquet faucibus ultricies. Morbi semper, est id tincidunt gravida, sem arcu adipiscing lacus, ac bibendum nulla leo eu purus. Quisque nec diam sed risus consectetur a ccumsan quis quis nibh. Vestibulum id purus lorem.</p>
    <p>It is a long established fact that a reader will be distracted by the readable content of a page when looking at its layout. The point of using Lorem Ipsum is that it has a more-or-less normal distribution of letters, as opposed to using 'Content here, content here', making it look like readable English. Many desktop publishing packages</p>
    <p>ada ut, consequat et diam. Nullam erat sem, rhoncus id ullamcorper vitae, rhoncus et arcu. In ultricies ultricies nulla, ut rutrum nisi iaculis at. Donec eu magna a metus ornare faucibus. Fusce aliquet faucibus ultricies. Morbi semper,</p>
    <div class="sign-off">Sincerely,</div>
    <span class="signature" role="img" aria-label="Handwritten signature of Sam Reid"></span>
  </section>
</article>

<article class="card card-front">
  <div class="card-motto">FINANCIAL PEACE OF MIND</div>
  <div class="card-motto-sub">A referral built business</div>
  <div class="card-person">
    <div class="person">
      <div class="person-name">SAM REID</div>
      <div class="person-cred">B.Ag.Ec. Dip F.P. CFP®</div>
      <div>Managing Director</div>
      <div>Authorised Representative</div>
    </div>
    <div class="card-contacts">
      <div class="contact-row"><svg class="icon"><use href="#i-phone"/></svg><span>(07) 3000 1234</span></div>
      <div class="contact-row"><svg class="icon"><use href="#i-mobile"/></svg><span>0400 123 456</span></div>
      <div class="contact-row"><svg class="icon"><use href="#i-fax"/></svg><span>(07) 3000 5678</span></div>
      <div class="contact-row"><svg class="icon"><use href="#i-mail"/></svg><span>sam@palomarfinancial.example</span></div>
      <div class="contact-row"><svg class="icon"><use href="#i-globe"/></svg><span>www.palomarfinancial.example</span></div>
    </div>
  </div>
  <div class="card-address">
    <div class="contact-row"><svg class="icon"><use href="#i-pin"/></svg><span>Suite 4A, 18 Harlow St, Riverbend QLD 4100</span></div>
    <div class="contact-row"><svg class="icon"><use href="#i-pin"/></svg><span>PO Box 5521, Eastvale QLD 4100</span></div>
  </div>
</article>

<article class="card card-back">
  <div class="brand">
    <div class="brand-circle"></div>
    <div class="brand-name">BLUEGATE WEALTH</div>
    <div class="brand-tag">Strategic Financial Advice</div>
  </div>
  <div class="services">Life &amp; TPD Insurance • Income Protection • Financial Planning</div>
  <div class="licensee-note"><span>Meridian Advice Partners limited</span>Australian Financial Services licensee License Number 000111</div>
</article>
</body>
</html>
```